Trovan Dirtworks LLC - Excavation Contractor in Idaho

Wordpress website, visually appealing....Company is Veteran owned business, owner SGT Harold Mensick USMC, anything from laser grading to cleaning up your property we do various Skidsteer work and are always buying new attachments to do more jobs. Services include: excavation, grading, snow plowing, demolition and cleanup, fence post hole drilling, trenching.

Target Market(s)

Contractors and Home owners needing projects completed

Industry/Entity Type

Construction

Number of Pages Required

3 page

Font styles to use
Sans Serif

Requirements
Must have
• Site visually appealing and easy to navigate.
Nice to have
• Maybe bold colors?

```html
<!DOCTYPE html>
<html lang="en">
<head>
<meta charset="utf-8">
<title>Trovan Dirtworks LLC – Excavation Contractor in Idaho</title>
<link href="https://fonts.googleapis.com/css2?family=Lato:ital,wght@0,400;0,700;0,900;1,400;1,700;1,900&display=swap" rel="stylesheet">
<style>
:root{
  --red:#c1121b;
  --red-dark:#5c0006;
  --ink:#1b1b1b;
  --text:#444;
  --grey-bg:#ebebeb;
  --footer:#111111;
  --white:#ffffff;
}
*{box-sizing:border-box;margin:0;padding:0}
html,body{width:1200px;height:5172px;overflow:hidden}
body{font-family:'Lato',sans-serif;color:var(--ink);background:#fff;position:relative}
section,header,footer,nav{position:absolute;left:0;width:1200px}

/* header */
.site-header{top:0;height:115px;background:#fff}
.brand{position:absolute;left:76px;top:38px;display:flex;align-items:center;gap:12px;font-weight:900;font-size:24px;color:var(--ink);letter-spacing:.5px}
.brand .mark{width:22px;height:22px;background:var(--red)}
.header-phone{position:absolute;left:862px;top:36px;display:flex;align-items:center;gap:20px}
.phone-box{width:50px;height:46px;background:var(--ink);display:flex;align-items:center;justify-content:center;transform:skewX(-8deg)}
.header-phone span{color:var(--red);font-weight:700;font-size:26px}

.main-nav{top:115px;height:65px;background:var(--red);display:flex;justify-content:center;align-items:center;gap:42px}
.main-nav a{color:#fff;text-decoration:none;font-weight:700;font-size:15px;text-transform:uppercase}

/* hero */
.hero{top:180px;height:648px;background:linear-gradient(180deg,#6f7074 0%,#8a8b8c 45%,#5c5646 75%,#4c4737 100%)}
.hero-name{position:absolute;top:210px;width:100%;text-align:center;color:#fff;font-weight:900;font-size:70px;letter-spacing:1px}
.hero-tag{position:absolute;top:338px;width:100%;text-align:center;color:#fff;font-weight:700;font-size:31px}
.btn{position:absolute;z-index:1;display:flex;align-items:center;justify-content:center;font-weight:700;font-size:17px;color:#1b1b1b;text-transform:uppercase}
.btn::before{content:"";position:absolute;inset:0;background:linear-gradient(180deg,#d9d9d9,#8d8d8d);border:2px solid #555;transform:skewX(-12deg);z-index:-1}

/* welcome */
.welcome{top:828px;height:586px;background:#fff}
.welcome-photo{position:absolute;left:76px;top:74px;width:509px;height:432px;background:linear-gradient(160deg,#aab4bd,#7f8c73 55%,#5a6244);clip-path:polygon(4% 0,100% 0,96% 100%,0 100%)}
h2.sec-title{font-weight:900;font-style:italic;font-size:36px;text-transform:uppercase;line-height:1}
.rule{width:104px;height:4px;background:var(--red)}
.welcome-text{position:absolute;left:618px;top:60px;width:520px;display:flex;flex-direction:column;align-items:flex-start}
.welcome-text h2.sec-title{font-size:34px;line-height:1.15;color:var(--ink)}
.welcome-text .rule{margin:16px 0 22px}
.welcome-text p{font-size:17px;line-height:33px;color:var(--text);margin-bottom:30px}
.welcome-text .btn{position:relative;margin-left:4px}

/* services */
.services{top:1414px;height:922px;background:linear-gradient(120deg,#8a0410 0%,#5c0006 50%,#b90d18 100%)}
.services h2{position:absolute;top:90px;width:100%;text-align:center;color:#fff}
.services .rule{position:absolute;left:548px;top:146px}
.card{position:absolute;width:328px;height:296px;overflow:hidden}
.card-photo{height:220px}
.card-label{height:76px;background:var(--red);color:#fff;font-weight:700;font-size:21px;display:flex;align-items:center;justify-content:center;text-transform:uppercase}
.card-overlay{position:absolute;inset:0;background:linear-gradient(180deg,#4a4c52,#2b2c30);color:#fff;text-align:center;padding:44px 24px 0}
.card-overlay h3{font-size:21px;font-weight:700;text-transform:uppercase;margin-bottom:10px}
.card-overlay p{font-size:13px;line-height:25px;color:#ddd}

/* projects */
.projects{top:2336px;height:694px;background:#fff}
.projects h2{position:absolute;left:76px;top:74px}
.projects p{position:absolute;left:80px;top:152px;width:300px;font-size:17px;line-height:28px;color:var(--text)}
.tile{position:absolute}

/* reviews */
.reviews{top:3030px;height:486px;background:var(--grey-bg)}
.reviews h2{position:absolute;top:76px;width:100%;text-align:center}
.reviews .rule{position:absolute;left:565px;top:136px}
.review{position:absolute;top:180px;width:520px;text-align:center}
.quote-icon{width:52px;height:44px;background:var(--red);margin:0 auto 20px;display:flex;align-items:center;justify-content:center}
.review p{font-style:italic;font-size:17px;line-height:31px;color:var(--text)}
.review h4{margin-top:18px;font-size:15px;font-weight:700;color:var(--red);text-transform:uppercase}

/* blog */
.blog{top:3516px;height:562px;background:#fff}
.blog h2{position:absolute;top:54px;width:100%;text-align:center;font-weight:900;font-size:36px;text-transform:uppercase}
.blog .rule{position:absolute;left:565px;top:106px}
.post{position:absolute;top:158px;width:328px;height:332px;color:#fff;text-align:center}
.post .shade{position:absolute;left:0;right:0;bottom:0;height:160px;background:linear-gradient(180deg,rgba(0,0,0,0),rgba(0,0,0,.85))}
.post h3{position:absolute;left:0;right:0;top:226px;font-size:16px;font-weight:700;line-height:27px;text-transform:uppercase}
.post time{position:absolute;left:0;right:0;top:296px;font-size:16px;font-weight:700}

/* quote form */
.quote{top:4078px;height:657px;background:linear-gradient(135deg,#1a0204 0%,#3e0307 40%,#7a0a12 70%,#2a0205 100%)}
.quote h2{position:absolute;top:80px;width:100%;text-align:center;color:#fff}
.quote .lead{position:absolute;top:166px;width:100%;text-align:center;color:#e6e6e6;font-size:17px}
.field{position:absolute;background:#fff;border:1px solid #ccc;font-size:15px;color:#333;padding:18px 20px}

/* footer */
.site-footer{top:4735px;height:437px;background:var(--footer);color:#ddd}
.footer-brand{position:absolute;left:80px;top:122px;display:flex;align-items:center;gap:10px;font-weight:900;font-size:19px;color:#fff}
.footer-brand .mark{width:18px;height:18px;background:var(--red)}
.copy{position:absolute;left:76px;top:198px;font-size:13px;line-height:25px;color:#bbb}
.social{position:absolute;left:76px;top:258px;display:flex;gap:22px}
.social span{width:26px;height:26px;border-radius:50%;border:2px solid #ddd}
.f-col{position:absolute;top:64px}
.f-col h5{font-size:16px;font-weight:900;color:#fff;text-transform:uppercase;margin-bottom:14px}
.f-col li{list-style:none;font-size:15px;line-height:40.5px;color:#ddd}
.contact-row{display:flex;gap:18px;font-size:15px;line-height:28px;margin-bottom:12px}
.contact-row svg{flex:none;margin-top:6px}
</style>
</head>
<body>

<header class="site-header">
  <div class="brand"><span class="mark"></span>TROVAN DIRTWORKS LLC</div>
  <div class="header-phone">
    <div class="phone-box"><svg width="22" height="22" viewBox="0 0 24 24"><path fill="#fff" d="M6.6 10.8a15.1 15.1 0 0 0 6.6 6.6l2.2-2.2a1 1 0 0 1 1-.25 11.4 11.4 0 0 0 3.6.57 1 1 0 0 1 1 1V20a1 1 0 0 1-1 1A17 17 0 0 1 3 4a1 1 0 0 1 1-1h3.5a1 1 0 0 1 1 1c0 1.25.2 2.45.57 3.57a1 1 0 0 1-.25 1z"/></svg></div>
    <span>1-800-555-0142</span>
  </div>
</header>

<nav class="main-nav">
  <a>Home</a><a>About Us</a><a>Services</a><a>Projects</a><a>Blog</a><a>Reviews</a><a>Contact Us</a>
</nav>

<section class="hero" role="img" aria-label="Tracked skid steer loader with snow pusher attachment on a field under an overcast sky">
  <div class="hero-name">TROVAN DIRTWORKS LLC</div>
  <div class="hero-tag">We are an Excavation Contractor in Idaho</div>
  <a class="btn" style="left:470px;top:410px;width:270px;height:56px">Book a Consultation</a>
</section>

<section class="welcome">
  <div class="welcome-photo" role="img" aria-label="Compact track loader parked on a gravel lot"></div>
  <div class="welcome-text">
    <h2 class="sec-title">Welcome to Trovan Dirtworks LLC</h2>
    <div class="rule"></div>
    <p>Sed ut perspiciatis unde omnis iste natus error sit voluptatem accusantium doloremque laudantium, totam rem aperiam, eaque ipsa quae ab illo inventore veritatis et quasi architecto beatae vitae dicta sunt explicaboemo enim ipsam voluptatem quia. Excepteur sint occaecat cupidatat non proident, sunt in culpa qui officia deserunt mollit anim id est laborum.</p>
    <a class="btn" style="width:206px;height:58px">Read More</a>
  </div>
</section>

<section class="services">
  <h2 class="sec-title">Our Services</h2>
  <div class="rule"></div>

  <div class="card" style="left:76px;top:204px">
    <div class="card-overlay" role="img" aria-label="Excavation work photo under dark overlay">
      <h3>Excavation</h3>
      <p>Sed ut perspiciatis unde omnis iste natus error sit voluptatem accusantium doloremque laudantium, totam rem aperiam.</p>
    </div>
    <a class="btn" style="left:90px;top:208px;width:150px;height:40px;font-size:13px">Read More</a>
  </div>
  <div class="card" style="left:436px;top:204px">
    <div class="card-photo" role="img" aria-label="Track loader grading soil beside a house build" style="background:linear-gradient(180deg,#c9b89a,#8a7050)"></div>
    <div class="card-label">Grading</div>
  </div>
  <div class="card" style="left:798px;top:204px">
    <div class="card-photo" role="img" aria-label="Wheel loader clearing snow under a blue sky" style="background:linear-gradient(180deg,#3a7fd1,#9ec6ea 60%,#e8eef4)"></div>
    <div class="card-label">Snow Plowing</div>
  </div>
  <div class="card" style="left:76px;top:530px">
    <div class="card-photo" role="img" aria-label="Excavator demolishing a wooden building" style="background:linear-gradient(180deg,#b8a58a,#6e5440)"></div>
    <div class="card-label">Demolition &amp; Cleanup</div>
  </div>
  <div class="card" style="left:436px;top:530px">
    <div class="card-photo" role="img" aria-label="Track loader with auger drilling fence post holes" style="background:linear-gradient(180deg,#9db3c9,#5e6a52 60%,#4a4034)"></div>
    <div class="card-label">Fence Post Hole Drilling</div>
  </div>
  <div class="card" style="left:798px;top:530px">
    <div class="card-photo" role="img" aria-label="Excavator digging a deep trench" style="background:linear-gradient(180deg,#6da3dc,#b7cde0 40%,#8a5a48)"></div>
    <div class="card-label">Trenching</div>
  </div>
</section>

<section class="projects">
  <h2 class="sec-title">Our Projects</h2>
  <p>Sed ut perspiciatis unde omnis iste natus error sit voluptatem accusa ntium doloremqueteur.</p>
  <a class="btn" style="left:80px;top:260px;width:210px;height:62px">View All</a>
  <div class="tile" style="left:426px;top:80px;width:348px;height:268px;background:linear-gradient(180deg,#93aac4,#7a6a52)" role="img" aria-label="Loader beside a dumpster on a cleared lot"></div>
  <div class="tile" style="left:778px;top:80px;width:349px;height:268px;background:linear-gradient(180deg,#8c9aa8,#5d5a4a)" role="img" aria-label="Track loader with bucket near power lines"></div>
  <div class="tile" style="left:76px;top:354px;width:346px;height:270px;background:linear-gradient(180deg,#c8a9a0,#6a8a48 55%,#3f5a2a)" role="img" aria-label="Green field with fresh trench at sunset"></div>
  <div class="tile" style="left:426px;top:354px;width:348px;height:270px;background:linear-gradient(180deg,#7d8a70,#4a4232)" role="img" aria-label="Track loader in a wooded yard"></div>
  <div class="tile" style="left:778px;top:354px;width:349px;height:270px;background:linear-gradient(180deg,#6f8468,#3e3a2c)" role="img" aria-label="Track loader with mulcher among pine trees"></div>
</section>

<section class="reviews">
  <h2 class="sec-title">Customer Reviews</h2>
  <div class="rule"></div>
  <div class="review" style="left:70px">
    <div class="quote-icon"><svg width="30" height="22" viewBox="0 0 30 22"><path fill="#fff" d="M2 0h11v10l-6 12H2l5-12H2zM17 0h11v10l-6 12h-5l5-12h-5z"/></svg></div>
    <p>" Sed ut perspiciatis unde omnis iste natus error sit voluptatem accusantium doloremque laudantium, totam rem aperiam, eaque ipsa quae ab illo inventore veritatis et quasi architecto beatae vitae dicta sunt explicabo.."</p>
    <h4>Name Heading</h4>
  </div>
  <div class="review" style="left:610px">
    <div class="quote-icon"><svg width="30" height="22" viewBox="0 0 30 22"><path fill="#fff" d="M2 0h11v10l-6 12H2l5-12H2zM17 0h11v10l-6 12h-5l5-12h-5z"/></svg></div>
    <p>" Sed ut perspiciatis unde omnis iste natus error sit voluptatem accusantium doloremque laudantium, totam rem aperiam, eaque ipsa quae ab illo inventore veritatis et quasi architecto beatae vitae dicta sunt explicabo.."</p>
    <h4>Name Heading</h4>
  </div>
</section>

<section class="blog">
  <h2>Blog Posts</h2>
  <div class="rule"></div>
  <article class="post" style="left:76px;background:linear-gradient(180deg,#3a3a3e,#151515)" role="img" aria-label="Loader working at night under lights">
    <div class="shade"></div><h3>Nemo enim ipsam voluptatem<br>quia voluptas</h3><time>Nov18, 2021</time>
  </article>
  <article class="post" style="left:436px;background:linear-gradient(180deg,#8d9aab,#2a4a80 60%,#1a1a1a)" role="img" aria-label="Excavator loading debris into a blue dumpster">
    <div class="shade"></div><h3>Nemo enim ipsam voluptatem<br>quia voluptas</h3><time>Nov18, 2021</time>
  </article>
  <article class="post" style="left:798px;background:linear-gradient(180deg,#a8b0b8,#6a6a64 55%,#1a1a1a)" role="img" aria-label="Blue dumpster beside a metal building">
    <div class="shade"></div><h3>Nemo enim ipsam voluptatem<br>quia voluptas</h3><time>Nov18, 2021</time>
  </article>
</section>

<section class="quote" role="img" aria-label="Red tinted background of a skid steer loader">
  <h2 class="sec-title">Request a Quote</h2>
  <p class="lead">Sed ut perspiciatis unde omnis iste natus error sit voluptatem accusantium doloremque.</p>
  <div class="field" style="left:164px;top:224px;width:420px;height:54px">Name</div>
  <div class="field" style="left:614px;top:224px;width:421px;height:54px">Email Address</div>
  <div class="field" style="left:164px;top:294px;width:420px;height:54px">Phone No</div>
  <div class="field" style="left:614px;top:294px;width:421px;height:54px">Subject</div>
  <div class="field" style="left:164px;top:364px;width:871px;height:136px">Message</div>
  <a class="btn" style="left:496px;top:516px;width:208px;height:58px">Submit Now</a>
</section>

<footer class="site-footer">
  <div class="footer-brand"><span class="mark"></span>TROVAN DIRTWORKS LLC</div>
  <p class="copy">Copyright ©2021 Trovan Dirtworks LLC.<br>All Rights Reserved.</p>
  <div class="social"><span></span><span></span><span></span><span></span><span></span></div>

  <div class="f-col" style="left:364px">
    <h5>Site Map</h5>
    <ul><li>Home</li><li>About Us</li><li>Services</li><li>Projects</li><li>Blog</li><li>Reviews</li><li>Contact Us</li></ul>
  </div>
  <div class="f-col" style="left:614px">
    <h5>Services</h5>
    <ul><li>Excavation</li><li>Grading</li><li>Snow plowing</li><li>Demolition and cleanup</li><li>Fence post hole drilling</li><li>Trenching</li></ul>
  </div>
  <div class="f-col" style="left:886px;width:280px">
    <h5>Contact Us</h5>
    <div class="contact-row"><svg width="14" height="18" viewBox="0 0 14 18"><path fill="#ddd" d="M7 0a7 7 0 0 0-7 7c0 5 7 11 7 11s7-6 7-11a7 7 0 0 0-7-7zm0 9.5A2.5 2.5 0 1 1 7 4.5a2.5 2.5 0 0 1 0 5z"/></svg><span>2210 Basalt Ridge Road,<br>Nampa, ID 83686</span></div>
    <div class="contact-row"><svg width="16" height="16" viewBox="0 0 24 24"><path fill="#ddd" d="M6.6 10.8a15.1 15.1 0 0 0 6.6 6.6l2.2-2.2a1 1 0 0 1 1-.25 11.4 11.4 0 0 0 3.6.57 1 1 0 0 1 1 1V20a1 1 0 0 1-1 1A17 17 0 0 1 3 4a1 1 0 0 1 1-1h3.5a1 1 0 0 1 1 1c0 1.25.2 2.45.57 3.57a1 1 0 0 1-.25 1z"/></svg><span>1-208-555-0177</span></div>
    <div class="contact-row"><svg width="16" height="14" viewBox="0 0 16 12"><path fill="#ddd" d="M0 0h16v2L8 7 0 2zM0 4l8 5 8-5v8H0z"/></svg><span>info@trovandirtworks.com</span></div>
  </div>
</footer>

</body>
</html>
```